Tervolan Pty Ltd professional business card

A professional business card template using the colours from the supplied logo.
Clean crisp lines while, Modern while not being over the top.

Target Market(s)

Construction, commerical and industrial

Industry/Entity Type

Communications

Contact Information for Business Card

For a Communications, IT, Optical fibre installation company

Colors
37b8a4

```html
<!DOCTYPE html>
<html lang="en">
<head>
<meta charset="utf-8">
<title>Tervolan Pty Ltd – Business Card</title>
<link href="https://fonts.googleapis.com/css2?family=Bebas+Neue&display=swap" rel="stylesheet">
<style>
  :root {
    --teal: #1591a0;
    --grey: #6d6e71;
    --white: #ffffff;
    --backdrop: #e4e4e4;
  }
  * { margin: 0; padding: 0; box-sizing: border-box; }
  html, body {
    width: 1200px;
    height: 1200px;
    overflow: hidden;
    background: var(--backdrop);
    font-family: "Bebas Neue", "Arial Narrow", sans-serif;
  }
  .canvas { position: relative; width: 1200px; height: 1200px; }
  .card {
    position: absolute;
    left: 252px;
    width: 696px;
    height: 398px;
    border-radius: 25px;
    background: var(--teal);
    overflow: hidden;
  }
  .card--front { top: 163px; }
  .card--back { top: 638px; }
  .card__frame { position: absolute; inset: 0; }
  .card__panel {
    position: absolute;
    background: var(--white);
    border-radius: 19px;
  }
  .card--front .card__panel { left: 52px; top: 30px; width: 592px; height: 338px; }
  .card--back .card__panel { left: 49px; top: 28px; width: 598px; height: 340px; }

  .wordmark {
    position: absolute;
    display: flex;
    align-items: center;
    gap: 12px;
    color: var(--grey);
    letter-spacing: 2px;
    line-height: 1;
    white-space: nowrap;
  }
  .wordmark__dot {
    border-radius: 50%;
    background: var(--teal);
    flex: none;
  }
  .card--front .wordmark { left: 50%; top: 50%; transform: translate(-50%, -50%); font-size: 112px; }
  .card--front .wordmark__dot { width: 34px; height: 34px; }
  .card--back .wordmark { left: 149px; top: 182px; transform: translate(-50%, -50%); font-size: 66px; }
  .card--back .wordmark__dot { width: 21px; height: 21px; }

  .divider {
    position: absolute;
    left: 296px;
    top: 14px;
    width: 5px;
    height: 312px;
    border-radius: 50%;
    background: var(--teal);
  }
  .contact-list {
    position: absolute;
    left: 334px;
    top: 48px;
    list-style: none;
  }
  .contact-list__item {
    display: flex;
    align-items: center;
    height: 61px;
    color: var(--teal);
    font-size: 38px;
    line-height: 1;
    white-space: nowrap;
  }
  .contact-list__icon {
    width: 26px;
    height: 26px;
    margin-right: 33px;
    fill: var(--grey);
    flex: none;
  }
</style>
</head>
<body>
<main class="canvas">

  <section class="card card--front" aria-label="Card front">
    <div class="card__frame" role="img" aria-label="Teal border where a repeating brand pattern belongs"></div>
    <div class="card__panel">
      <div class="wordmark"><span class="wordmark__dot"></span>Tervolan</div>
    </div>
  </section>

  <section class="card card--back" aria-label="Card back">
    <div class="card__frame" role="img" aria-label="Teal border where a repeating brand pattern belongs"></div>
    <div class="card__panel">
      <div class="wordmark"><span class="wordmark__dot"></span>Tervolan</div>
      <div class="divider"></div>
      <ul class="contact-list">
        <li class="contact-list__item">
          <svg class="contact-list__icon" viewBox="0 0 24 24" aria-hidden="true"><circle cx="12" cy="7" r="5"/><path d="M3 22v-3a5 5 0 0 1 5-5h8a5 5 0 0 1 5 5v3z"/></svg>
          Your Name
        </li>
        <li class="contact-list__item">
          <svg class="contact-list__icon" viewBox="0 0 24 24" aria-hidden="true"><path d="M6.6 10.8a15 15 0 0 0 6.6 6.6l2.2-2.2a1 1 0 0 1 1-.25 11.4 11.4 0 0 0 3.6.6 1 1 0 0 1 1 1V20a1 1 0 0 1-1 1A17 17 0 0 1 3 4a1 1 0 0 1 1-1h3.5a1 1 0 0 1 1 1c0 1.25.2 2.450.6 3.6a1 1 0 0 1-.25 1z"/></svg>
          Your Phone
        </li>
        <li class="contact-list__item">
          <svg class="contact-list__icon" viewBox="0 0 24 24" aria-hidden="true"><path d="M12 1a8 8 0 0 0-8 8c0 6 8 14 8 14s8-8 8-14a8 8 0 0 0-8-8zm0 11a3 3 0 1 1 0-6 3 3 0 0 1 0 6z"/></svg>
          Your Location
        </li>
        <li class="contact-list__item">
          <svg class="contact-list__icon" viewBox="0 0 24 24" aria-hidden="true"><path d="M2 5h20v14H2zm2 2v.4l8 5.6 8-5.6V7zm0 2.8V17h16V9.8l-8 5.6z"/></svg>
          Your Email
        </li>
      </ul>
    </div>
  </section>

</main>
</body>
</html>
```